Corlath Landscaping - WebSite
I like the rounded edges like in draft #18 and #20. Also like the use of the logo's in #20. I like the menu bars in #18 too.
Can you guys add a "Pay Now" graphic. It doesn't need to be those exact words, but I'd like to be able to send users to the site and click on that link to pay a one time bill or signup for AutoPay. Thanks!!!
Hey guys. Thanks for submitting the drafts. They look great.
I have been so busy that I have just been able to take a quick look. I haven't gotten a chance to provide feedback and answer questions. I need to extend the contest. I'll provide feedback tomorrow. Thanks!!!

```html
<!DOCTYPE html>
<html lang="en">
<head>
<meta charset="utf-8">
<title>Corlath Landscaping – Maintenance Services</title>
<link href="https://fonts.googleapis.com/css2?family=Arimo:wght@400;700&display=swap" rel="stylesheet">
<style>
:root{
  --page-bg:#e4efd2;
  --page-bg-2:#cfe2ad;
  --forest:#2f4a12;
  --forest-dark:#22370b;
  --leaf:#8db43a;
  --leaf-light:#b8d67a;
  --title-green:#4f7a16;
  --body-text:#7a7a7a;
  --white:#ffffff;
  --footer-bg:#d9e8bf;
  --footer-line:#b9cf92;
  --rose:#f0b81c;
}
*{box-sizing:border-box;margin:0;padding:0}
html,body{width:1200px;height:1086px;overflow:hidden}
body{font-family:"Arimo",Arial,sans-serif;background:linear-gradient(180deg,var(--page-bg) 0%,var(--page-bg-2) 60%,var(--page-bg) 100%);position:relative;color:var(--body-text)}
.leaf-photo{position:absolute;left:0;top:120px;width:230px;height:330px;background:radial-gradient(ellipse at 30% 45%,#9cc94a 0%,#6e9f25 40%,rgba(180,210,120,0) 75%)}
.brand{position:absolute;left:210px;top:30px;display:flex;align-items:center;gap:14px}
.brand-dot{width:52px;height:52px;border-radius:50%;background:var(--forest)}
.brand-name{font-weight:700;font-size:34px;line-height:1;color:var(--forest);letter-spacing:1px}
.utility-nav{position:absolute;left:825px;top:0;width:261px;height:32px;background:var(--forest);border-radius:0 0 16px 16px;display:flex;justify-content:center;gap:40px;align-items:center}
.utility-nav a,.main-nav a{color:var(--white);text-decoration:none;font-weight:700;font-size:13px;letter-spacing:.5px}
.pay-now{position:absolute;left:966px;top:56px;width:120px;height:30px;border-radius:15px;background:var(--leaf);color:var(--white);font-weight:700;font-size:13px;letter-spacing:.5px;text-align:center;line-height:30px;text-decoration:none}
.main-nav{position:absolute;left:495px;top:116px;width:591px;height:34px;background:var(--forest);border-radius:16px 16px 0 0;display:flex;justify-content:space-around;align-items:center;padding:0 10px}
.main-panel{position:absolute;left:150px;top:186px;width:936px;height:724px;background:var(--forest);border-radius:0 20px 20px 20px}
.content-card{position:absolute;left:36px;top:10px;width:630px;height:670px;background:var(--white);border-radius:6px;overflow:hidden}
.section-bar{background:var(--leaf);color:var(--white);font-weight:700;font-size:15px;padding:8px 14px;letter-spacing:.5px}
.content-body{padding:16px 14px}
.intro{color:var(--title-green);font-weight:700;font-size:16px}
.intro-sub{color:var(--title-green);font-size:12px;margin-bottom:14px}
.content-body p{font-size:11px;line-height:14px;margin-bottom:14px;text-align:justify}
.rose-photo{position:absolute;left:690px;top:10px;width:240px;height:272px;border-radius:8px;background:radial-gradient(circle at 50% 45%,#fbe07a 0%,var(--rose) 45%,#d08a10 100%)}
.quote-label{position:absolute;left:700px;top:296px;color:var(--leaf-light);font-weight:700;font-size:13px;letter-spacing:.5px}
.quote-form{position:absolute;left:700px;top:318px;width:222px;height:382px;background:var(--white);border-radius:6px;padding:14px 12px}
.quote-form label{display:block;font-size:13px;font-weight:700;color:var(--forest-dark);margin-top:6px}
.field{height:28px;border-radius:4px;background:linear-gradient(180deg,#e6e6e6,#fafafa);border:1px solid #d2d2d2;margin:4px 0 10px}
.field.tall{height:90px}
.continue{display:block;margin:14px auto 0;width:120px;height:30px;border-radius:15px;background:var(--forest);color:var(--white);font-weight:700;font-size:13px;text-align:center;line-height:30px}
.form-mark{position:absolute;right:12px;bottom:12px;font-weight:700;font-size:13px;color:#c9dba8}
.site-footer{position:absolute;left:0;top:930px;width:1200px;height:156px;background:var(--footer-bg);border-top:1px solid var(--footer-line)}
.footer-col{position:absolute;top:14px}
.footer-col h3{font-size:17px;font-weight:400;color:var(--forest-dark);margin-bottom:8px}
.tips{left:150px;width:230px;text-align:center}
.tips p{font-size:11px;font-weight:700;color:#555;text-align:left;line-height:14px}
.share{left:520px;width:240px}
.share h3{text-align:center}
.share ul,.links ul{list-style:none}
.share li{display:flex;align-items:center;gap:8px;font-size:11px;font-weight:700;color:#444;height:16px;margin-bottom:5px}
.share-icon{width:16px;height:16px;border-radius:50%;background:var(--forest);flex:none}
.links{left:870px;width:216px;text-align:right}
.links h3{text-align:right}
.links li{font-size:12px;font-weight:700;color:var(--forest-dark);padding:3px 0;border-bottom:1px solid var(--footer-line);text-align:left;margin-left:110px}
.copyright{position:absolute;left:0;width:1200px;top:130px;text-align:center;font-size:9px;color:#555;line-height:11px}
</style>
</head>
<body>
<div class="leaf-photo" role="img" aria-label="Close-up photograph of fresh green leaves on a branch"></div>

<header>
  <div class="brand"><span class="brand-dot"></span><span class="brand-name">CORLATH<br>LANDSCAPING</span></div>
  <nav class="utility-nav"><a href="#">HOME</a><a href="#">CONTACT US</a></nav>
  <a class="pay-now" href="#">PAY NOW</a>
  <nav class="main-nav"><a href="#">ABOUT US</a><a href="#">MAINTENANCE</a><a href="#">INSTALLATION</a><a href="#">PHOTO GALLERY</a></nav>
</header>

<main class="main-panel">
  <section class="content-card">
    <div class="section-bar">MAINTENANCE SERVICES</div>
    <div class="content-body">
      <div class="intro">This can be introductory text</div>
      <div class="intro-sub">This can be a second line of text</div>
      <p>Lorem ipsum dolor sit amet consectetur adipiscing elit sed do eiusmod tempor incididunt ut labore et dolore magna aliqua ut enim ad minim veniam quis nostrud exercitation ullamco laboris nisi aliquip.</p>
      <p>Lorem ipsum dolor sit amet consectetur adipiscing elit sed do eiusmod tempor incididunt ut labore et dolore magna aliqua ut enim ad minim veniam quis nostrud exercitation ullamco laboris nisi aliquip. Lorem ipsum dolor sit amet consectetur adipiscing elit sed do eiusmod tempor incididunt ut labore et dolore magna aliqua ut enim ad minim veniam quis nostrud exercitation ullamco laboris nisi aliquip. Lorem ipsum dolor sit amet consectetur adipiscing elit sed do eiusmod tempor incididunt ut labore et dolore magna aliqua ut enim ad minim veniam quis nostrud exercitation ullamco laboris nisi aliquip. Lorem ipsum dolor sit amet consectetur adipiscing elit sed do eiusmod tempor incididunt ut labore et dolore magna aliqua ut enim ad minim veniam quis nostrud exercitation ullamco laboris nisi aliquip.</p>
      <p>Lorem ipsum dolor sit amet consectetur adipiscing elit sed do eiusmod tempor incididunt ut labore et dolore magna aliqua ut enim ad minim veniam quis nostrud exercitation ullamco laboris nisi aliquip. Lorem ipsum dolor sit amet consectetur adipiscing elit sed do eiusmod tempor incididunt ut labore et dolore magna aliqua ut enim ad minim veniam quis nostrud exercitation ullamco laboris nisi aliquip.</p>
      <p>Lorem ipsum dolor sit amet consectetur adipiscing elit sed do eiusmod tempor incididunt ut labore et dolore magna aliqua ut enim ad minim veniam quis nostrud exercitation ullamco laboris nisi aliquip. Lorem ipsum dolor sit amet consectetur adipiscing elit sed do eiusmod tempor incididunt ut labore et dolore magna aliqua ut enim ad minim veniam quis nostrud exercitation ullamco laboris nisi aliquip. Lorem ipsum dolor sit amet consectetur adipiscing elit sed do eiusmod tempor incididunt ut labore et dolore magna aliqua ut enim ad minim veniam quis nostrud exercitation ullamco laboris nisi aliquip.</p>
    </div>
  </section>

  <div class="rose-photo" role="img" aria-label="Close-up photograph of a yellow rose in bloom"></div>

  <div class="quote-label">BUILD A QUOTE</div>
  <form class="quote-form">
    <label>Name</label><div class="field"></div>
    <label>Email</label><div class="field"></div>
    <label>Message</label><div class="field tall"></div>
    <span class="continue">CONTINUE</span>
    <span class="form-mark">CORLATH</span>
  </form>
</main>

<footer class="site-footer">
  <div class="footer-col tips">
    <h3>Lawn Care Tips</h3>
    <p>“ Keeping a lawn healthful all season long does not need to be complicated - keep grass maintenance simple with a quick and easy lawn primer ”</p>
  </div>
  <div class="footer-col share">
    <h3>Share with Others</h3>
    <ul>
      <li><span class="share-icon"></span>Be a fan on Plazabook</li>
      <li><span class="share-icon"></span>Follow us on Chirper</li>
      <li><span class="share-icon"></span>Email a Friend</li>
      <li><span class="share-icon"></span>+1 on Circleo</li>
    </ul>
  </div>
  <div class="footer-col links">
    <h3>Quick Links</h3>
    <ul>
      <li>About us</li>
      <li>Maintenance</li>
      <li>Installation</li>
      <li>Contact us</li>
    </ul>
  </div>
  <div class="copyright">© 2011 Corlath Landscaping. All Rights Reserved<br>Privacy Policy | Terms of Use</div>
</footer>
</body>
</html>
```